Transfer Falcon - Cloud Based Data Migration Service for IT Professionals

We are looking for a smart clean website design for an informational site about our services and as a main portal into the service itself. We would like the design completed in WORDPRESS so that it will easily connect with the service.

Transfer Falcon is a cloud based migration service providing (to start with) a online migration tool that we migrate Quillnet Relay mailboxes (email) with all the settings, attachments from one system to another.
The service is aimed at IT professionals, IT companies and IT departments so our customers will be very technology based.

The Service -
IT companies currently migrate email; data and databases. using a very time intensive process which is both expensive and means their customer potentially losses access to its IT for a significant period of time. Additionally there are risks with regards to compatibility between systems and loss of data.
Potential benefits include;
• cost savings
• improved customer service, including reduced downtime
• improved resilience of the process
We are therefore developing cloud based migration software/website which will automate the process, mitigating these issues, as well as providing additional benefits such as the ability to sort and migrate only certain areas of data or certain emails, to check the integrity of the data/emails moved and to also repair corrupted data and emails.
The system will effectively duplicate the data and emails onto the new system over the weeks prior to the completion date. This will enable the IT Company to complete a final synchronisation and then immediately switch over to the new system with no interruption to the end users.
There is also an added benefit that the end users can test the system (with their own data and emails) prior to the switch over date to ensure everything is in place and databases work correctly.
The system will be completely cloud based and therefore easy for the IT Companies to access. They will be able to purchase the use of the system using CoinDrop or credit card and will only need to purchase what they need, this will allow even small local IT companies the facilities which previously would have been cost prohibitive to them.

Some of the sites we like for reference are -
Lanterbox, brightkits, the sky shifter.

We already have a logo design see attached and the website will need to work with this design.
Please message me if you have any questions
We do have the logo in other file formats if required.
Many Thanks

Target Market(s)

IT Sector

Industry/Entity Type

It Service

Number of Pages Required

5+ page

Requirements
Must have
• Front Page
• About Us
• Contact Info
• Blog
• Benefits
• More Information
• Must be Mobile Phone Compatible/friendly
• Log in (button) and support button on all pages (possibley top right)

```html
<!DOCTYPE html>
<html lang="en">
<head>
<meta charset="utf-8">
<title>Transfer Falcon</title>
<link href="https://fonts.googleapis.com/css2?family=Open+Sans:ital,wght@0,400;0,600;0,700;0,800;1,700;1,800&display=swap" rel="stylesheet">
<style>
:root{
  --ink:#333638;
  --brand-blue:#1aa3dd;
  --nav-bg:#2d3236;
  --white:#ffffff;
  --footer-bg:#000000;
  --dot-off:#d4d4d4;
  --hero-warm:#f7dfe1;
  --hero-mid:#fcf3f2;
  --tile-orange:#cd5c00;
  --tile-plum:#5a3364;
  --tile-lime:#8be534;
  --tile-mauve:#ab7eab;
  --tile-mustard:#c49e00;
  --tile-green:#4c9a08;
  --tile-red:#cc0000;
  --tile-navy:#224a85;
}
*{margin:0;padding:0;box-sizing:border-box}
html,body{width:1200px;height:2320px;overflow:hidden;background:var(--white)}
body{position:relative;font-family:"Open Sans",Arial,sans-serif;color:var(--ink)}

.site-header{position:absolute;left:0;top:0;width:1200px;height:196px;background:var(--white)}
.brand{position:absolute;left:124px;top:22px;display:flex;align-items:center;gap:24px;height:160px}
.brand-mark{width:160px;height:160px;border-radius:50%;background:var(--brand-blue);flex:none}
.brand-name{font-size:54px;font-weight:600;letter-spacing:16px;color:#1f1f1f;text-transform:uppercase;white-space:nowrap;line-height:1}

.main-nav{position:absolute;left:0;top:196px;width:1200px;height:78px;background:var(--nav-bg)}
.main-nav a{position:absolute;top:23px;font-size:24px;font-weight:700;color:var(--brand-blue);text-decoration:none;text-transform:uppercase;white-space:nowrap}

.hero{position:absolute;left:0;top:274px;width:1200px;height:638px;overflow:hidden}
.hero-photo{position:absolute;left:300px;top:0;width:900px;height:638px;
  background:linear-gradient(100deg,var(--white) 0%,var(--hero-mid) 55%,var(--hero-warm) 100%)}
.hero-title{position:absolute;left:102px;top:60px;font-size:68px;font-weight:700;color:var(--ink);line-height:1;white-space:nowrap}
.hero-sub{position:absolute;left:102px;top:134px;width:700px;font-size:24px;font-weight:700;line-height:28px;color:var(--ink);text-transform:uppercase}
.btn-service{position:absolute;left:104px;top:460px;width:419px;height:65px;background:var(--brand-blue);color:var(--white);font-size:22px;font-weight:700;text-align:center;line-height:65px;text-decoration:none}
.slider-dots{position:absolute;left:104px;top:554px;display:flex;gap:6px}
.slider-dots span{width:31px;height:31px;border-radius:50%;background:var(--brand-blue)}
.slider-dots span.off{background:var(--dot-off)}

.service-grid{position:absolute;left:104px;top:960px;display:grid;grid-template-columns:repeat(3,316px);grid-auto-rows:316px;column-gap:21px;row-gap:21px}
.service-tile{position:relative;color:var(--white);padding:68px 0 0 61px}
.service-tile.is-raised{padding-top:57px}
.tile-title{font-size:21px;font-weight:800;font-style:italic;text-transform:uppercase;line-height:1.2}
.tile-text{margin-top:22px;width:210px;font-size:17px;font-weight:700;line-height:22px}
.tile-more{position:absolute;left:61px;top:226px;font-size:16px;font-weight:800;font-style:italic;text-transform:uppercase;color:var(--white);text-decoration:none}
.is-raised .tile-more{top:215px}
.t-orange{background:var(--tile-orange)}
.t-plum{background:var(--tile-plum)}
.t-lime{background:var(--tile-lime)}
.t-mauve{background:var(--tile-mauve)}
.t-mustard{background:var(--tile-mustard)}
.t-green{background:var(--tile-green)}
.t-red{background:var(--tile-red)}
.t-navy{background:var(--tile-navy)}

.site-footer{position:absolute;left:0;top:2083px;width:1200px;height:237px;background:var(--footer-bg);color:var(--white)}
.footer-col{position:absolute;top:30px}
.footer-col h3{font-size:22px;font-weight:700;margin-bottom:8px}
.footer-col p{font-size:15px;line-height:29px;display:flex;align-items:center;gap:8px}
.address p{line-height:27px}
.social-dot{width:22px;height:22px;border-radius:50%;background:var(--brand-blue);flex:none}
.follow{left:400px}
.address{left:646px}
.copyright{position:absolute;left:400px;top:178px;font-size:15px}
</style>
</head>
<body>

<header class="site-header">
  <div class="brand">
    <span class="brand-mark"></span>
    <span class="brand-name">Transfer Falcon</span>
  </div>
</header>

<nav class="main-nav">
  <a href="#" style="left:102px">Home</a>
  <a href="#" style="left:213px">About Us</a>
  <a href="#" style="left:374px">Contact Info</a>
  <a href="#" style="left:591px">Blog</a>
  <a href="#" style="left:691px">Benefits</a>
  <a href="#" style="left:840px">More Information</a>
</nav>

<section class="hero">
  <div class="hero-photo" role="img" aria-label="Photo of a red data cable with a black connector on a white background"></div>
  <h1 class="hero-title">LOREM IPSUM DOLOR</h1>
  <p class="hero-sub">Lorem ipsum dolor sit amet, qui veri postea indoctum ei, at dicam malorum pri.</p>
  <a class="btn-service" href="#">VIEW SERVICE</a>
  <div class="slider-dots"><span></span><span></span><span class="off"></span><span></span></div>
</section>

<section class="service-grid">
  <article class="service-tile t-orange is-raised"><h2 class="tile-title">Ttitle goes here</h2><p class="tile-text">Lorem ipsum dolor sit amet, persius iudicabit explicari duo in.</p><a class="tile-more" href="#">Read more</a></article>
  <article class="service-tile t-plum"><h2 class="tile-title">Ttitle goes here</h2><p class="tile-text">Lorem ipsum dolor sit amet, persius iudicabit explicari duo in.</p><a class="tile-more" href="#">Read more</a></article>
  <article class="service-tile t-lime"><h2 class="tile-title">Ttitle goes here</h2><p class="tile-text">Lorem ipsum dolor sit amet, persius iudicabit explicari duo in.</p><a class="tile-more" href="#">Read more</a></article>
  <article class="service-tile t-mauve"><h2 class="tile-title">Ttitle goes here</h2><p class="tile-text">Lorem ipsum dolor sit amet, persius iudicabit explicari duo in.</p><a class="tile-more" href="#">Read more</a></article>
  <article class="service-tile t-mustard"><h2 class="tile-title">Ttitle goes here</h2><p class="tile-text">Lorem ipsum dolor sit amet, persius iudicabit explicari duo in.</p><a class="tile-more" href="#">Read more</a></article>
  <article class="service-tile t-orange"><h2 class="tile-title">Ttitle goes here</h2><p class="tile-text">Lorem ipsum dolor sit amet, persius iudicabit explicari duo in.</p><a class="tile-more" href="#">Read more</a></article>
  <article class="service-tile t-green"><h2 class="tile-title">Ttitle goes here</h2><p class="tile-text">Lorem ipsum dolor sit amet, persius iudicabit explicari duo in.</p><a class="tile-more" href="#">Read more</a></article>
  <article class="service-tile t-red"><h2 class="tile-title">Ttitle goes here</h2><p class="tile-text">Lorem ipsum dolor sit amet, persius iudicabit explicari duo in.</p><a class="tile-more" href="#">Read more</a></article>
  <article class="service-tile t-navy"><h2 class="tile-title">Ttitle goes here</h2><p class="tile-text">Lorem ipsum dolor sit amet, persius iudicabit explicari duo in.</p><a class="tile-more" href="#">Read more</a></article>
</section>

<footer class="site-footer">
  <div class="footer-col follow">
    <h3>Follow Us</h3>
    <p><span class="social-dot"></span>Like us on Friendwall</p>
    <p><span class="social-dot"></span>Follow us on Chirper</p>
    <p><span class="social-dot"></span>Follow us on Pinboardly</p>
  </div>
  <div class="footer-col address">
    <h3>Address</h3>
    <p>Name Surname</p>
    <p>01234567</p>
    <p>email@example.com</p>
    <p>www.falconsite.net</p>
    <p>Street, City, ZIP</p>
  </div>
  <p class="copyright">© by&nbsp; COMPANYNAME</p>
</footer>

</body>
</html>
```